Flyer Design Project

Need a DL Size flyer (2 sided) for letter box marketing for our website www.brightwardsecure.com.au
Updates

Project Deadline Extended
Reason: Thank you for submitting the designs. We like few of the designs and will request those designers to changes few things to make it more suitable for us. Because of holidays need to extend the deadlines. Thank you.

Industry/Entity Type

Marketing

```html
<!DOCTYPE html>
<html lang="en">
<head>
<meta charset="utf-8">
<title>Brightward Secure – Packages</title>
<link href="https://fonts.googleapis.com/css2?family=Arimo:wght@700&family=Roboto+Condensed:wght@400;700&display=swap" rel="stylesheet">
<style>
  :root {
    --head-top: #3a75b8;
    --head-bottom: #1f4f90;
    --row-light: #ececec;
    --row-dark: #dedede;
    --cell-text: #333333;
    --price: #1f7fc4;
    --band: #2f86c0;
    --band-dark: #1f6c9f;
    --paper: #ffffff;
    --photo-top: #f4f4f4;
    --photo-bottom: #d9dde2;
  }
  * { box-sizing: border-box; margin: 0; padding: 0; }
  html, body { width: 1200px; height: 772px; overflow: hidden; background: var(--paper); }
  .flyer { position: relative; width: 1200px; height: 772px; background: var(--paper); overflow: hidden; }
  .swoosh { position: absolute; left: 0; bottom: 0; width: 1200px; height: 300px; }
  .packages {
    position: absolute; left: 40px; top: 26px; width: 1120px;
    display: grid; grid-template-columns: repeat(6, 1fr); gap: 0 2px;
    box-shadow: 0 14px 22px -12px rgba(0,0,0,0.45);
  }
  .package { display: flex; flex-direction: column; background: var(--row-light); }
  .package-head {
    height: 76px; background: linear-gradient(var(--head-top), var(--head-bottom));
    color: #fff; text-align: center; font-family: "Arimo", Arial, sans-serif; font-weight: 700;
    padding-top: 6px;
  }
  .package-name { font-size: 21px; line-height: 26px; }
  .package-type { font-size: 14px; line-height: 16px; }
  .package-photo-wrap { height: 160px; padding: 8px 6px; background: var(--row-light); }
  .package-photo {
    width: 100%; height: 100%; border-radius: 8px; border: 1px solid #cfcfcf;
    background: linear-gradient(var(--photo-top), var(--photo-bottom));
  }
  .package-features { list-style: none; }
  .package-features li {
    height: 38px; display: flex; align-items: center; justify-content: center;
    font-family: "Roboto Condensed", "Arial Narrow", sans-serif; font-size: 13px;
    color: var(--cell-text); letter-spacing: -0.2px;
  }
  .package-features li:nth-child(odd) { background: var(--row-light); }
  .package-features li:nth-child(even) { background: var(--row-dark); }
  .package-price {
    height: 42px; display: flex; align-items: center; justify-content: center;
    background: var(--row-light); color: var(--price);
    font-family: "Roboto Condensed", "Arial Narrow", sans-serif; font-weight: 700; font-size: 20px;
  }
  .contact {
    position: absolute; right: 60px; bottom: 28px; display: flex; gap: 44px;
    color: #fff; font-family: "Arimo", Arial, sans-serif; font-weight: 700; font-size: 22px;
  }
  .contact-item { display: flex; align-items: center; gap: 10px; }
  .contact-item svg { fill: none; stroke: #fff; stroke-width: 2; }
</style>
</head>
<body>
<main class="flyer">
  <svg class="swoosh" viewBox="0 0 1200 300" preserveAspectRatio="none" aria-hidden="true">
    <defs>
      <linearGradient id="bandFill" x1="0" y1="0" x2="1" y2="1">
        <stop offset="0" stop-color="var(--band)"/>
        <stop offset="1" stop-color="var(--band-dark)"/>
      </linearGradient>
    </defs>
    <path d="M0 300 L0 250 C300 150 700 130 1200 100 L1200 300 Z" fill="url(#bandFill)"/>
  </svg>

  <section class="packages">
    <article class="package">
      <header class="package-head"><div class="package-name">Package 1</div><div class="package-type">Standalone DVR System<br>(2 Cameras)</div></header>
      <div class="package-photo-wrap"><div class="package-photo" role="img" aria-label="Monitor, DVR recorder and two dome cameras"></div></div>
      <ul class="package-features">
        <li>2 X high resolution dome cameras</li><li>1 X 4 channel standalone DVR</li><li>500GB hard drive</li><li>19" LCD monitor</li>
        <li>Remote access from PCs &amp; Phones*</li><li>Easy to use</li><li>1 Year Warranty</li><li>Full system supplied &amp; installed</li>
      </ul>
      <div class="package-price">$1495 + GST*</div>
    </article>
    <article class="package">
      <header class="package-head"><div class="package-name">Package 2</div><div class="package-type">Standalone DVR System<br>(4 Cameras)</div></header>
      <div class="package-photo-wrap"><div class="package-photo" role="img" aria-label="Monitor, DVR recorder and four dome cameras"></div></div>
      <ul class="package-features">
        <li>4 X high resolution dome cameras</li><li>1 X 4 channel standalone DVR</li><li>500GB hard drive</li><li>19" LCD monitor</li>
        <li>Remote access from PCs &amp; Phones*</li><li>Easy to use</li><li>1 Year Warranty</li><li>Full system supplied &amp; installed</li>
      </ul>
      <div class="package-price">$2195 + GST*</div>
    </article>
    <article class="package">
      <header class="package-head"><div class="package-name">Package 3</div><div class="package-type">Standalone DVR System<br>(8 Cameras)</div></header>
      <div class="package-photo-wrap"><div class="package-photo" role="img" aria-label="Monitor, DVR recorder and eight dome cameras"></div></div>
      <ul class="package-features">
        <li>8 X high resolution dome cameras</li><li>1 X 8 channel standalone DVR</li><li>1 Terrabyte hard drive</li><li>19" LCD monitor</li>
        <li>Remote access from PCs &amp; Phones*</li><li>Easy to use</li><li>1 Year Warranty</li><li>Full system supplied &amp; installed</li>
      </ul>
      <div class="package-price">$3295 + GST*</div>
    </article>
    <article class="package">
      <header class="package-head"><div class="package-name">Package 4</div><div class="package-type">IP based CCTV System<br>(2 Cameras)</div></header>
      <div class="package-photo-wrap"><div class="package-photo" role="img" aria-label="Monitor, PC tower, keyboard and two IP cameras"></div></div>
      <ul class="package-features">
        <li>2 X 2 Megapixel IP Cameras</li><li>1 X PC based NVR System</li><li>500GB hard drive</li><li>19" LCD monitor</li>
        <li>Remote access from PCs &amp; Phones*</li><li>Easy to use</li><li>1 Year Warranty</li><li>Full system supplied &amp; installed</li>
      </ul>
      <div class="package-price">$1995 + GST*</div>
    </article>
    <article class="package">
      <header class="package-head"><div class="package-name">Package 5</div><div class="package-type">IP based CCTV System<br>(4 Cameras)</div></header>
      <div class="package-photo-wrap"><div class="package-photo" role="img" aria-label="Monitor, PC tower, keyboard and four IP cameras"></div></div>
      <ul class="package-features">
        <li>4 X 2 Megapixel IP Cameras</li><li>1 X PC based NVR System</li><li>1 Terrabyte hard drive</li><li>19" LCD monitor</li>
        <li>Remote access from PCs &amp; Phones*</li><li>Easy to use</li><li>1 Year Warranty</li><li>Full system supplied &amp; installed</li>
      </ul>
      <div class="package-price">$3295 + GST*</div>
    </article>
    <article class="package">
      <header class="package-head"><div class="package-name">Package 6</div><div class="package-type">IP based CCTV System<br>(8 Cameras)</div></header>
      <div class="package-photo-wrap"><div class="package-photo" role="img" aria-label="Monitor, PC tower, keyboard and eight IP cameras"></div></div>
      <ul class="package-features">
        <li>8 X 2 Megapixel IP Cameras</li><li>1 X PC based NVR System</li><li>2 Terrabyte hard drive</li><li>19" LCD monitor</li>
        <li>Remote access from PCs &amp; Phones*</li><li>Easy to use</li><li>1 Year Warranty</li><li>Full system supplied &amp; installed</li>
      </ul>
      <div class="package-price">$4495 + GST*</div>
    </article>
  </section>

  <footer class="contact">
    <div class="contact-item">
      <svg width="26" height="22" viewBox="0 0 26 22" aria-hidden="true"><rect x="1" y="1" width="24" height="15" rx="1"/><path d="M13 16v4M7 21h12"/></svg>
      <span>www.brightwardsecure.com.au</span>
    </div>
    <div class="contact-item">
      <svg width="14" height="24" viewBox="0 0 14 24" aria-hidden="true"><rect x="1" y="1" width="12" height="22" rx="2"/><path d="M5 19h4"/></svg>
      <span>02 5550 1234</span>
    </div>
    <div class="contact-item">
      <svg width="30" height="20" viewBox="0 0 30 20" aria-hidden="true"><rect x="1" y="1" width="28" height="18"/><path d="M1 1l14 11L29 1M1 19l10-9M29 19l-10-9"/></svg>
      <span>hello@brightwardsecure.com.au</span>
    </div>
  </footer>
</main>
</body>
</html>
```